body balm label design

body balm tube design, current label design for other similar products
Need to have a design which can interchange between 3 different solutions
Amber Tide (Lavender + Vanilla)
Copper Harbor (Eucalyptus + Mint)
Velvet Arc (Bergamot + Cedarwood)
Tube size:
2.5h x 3.25 w
Target Market(s)
natural, solution focused
Requirements
Must have
- relatable to existing brand designs, focus on features and benefits

```html
<!DOCTYPE html>
<html lang="en">
<head>
<meta charset="utf-8">
<title>Body Balm Label Set</title>
<link href="https://fonts.googleapis.com/css2?family=Jost:ital,wght@0,400;0,500;1,400&family=Saira+Condensed:wght@400;500&display=swap" rel="stylesheet">
<style>
  :root {
    --backdrop: #dcdcdc;
    --backdrop-art: #e6e6e6;
    --paper: #ffffff;
    --lavender: #9a9ac5;
    --sage: #7b9a89;
    --olive: #7d7658;
    --art-lavender: #e4e4f0;
    --art-sage: #e1e9e4;
    --art-olive: #e7e5dc;
  }
  * { margin: 0; padding: 0; box-sizing: border-box; }
  html, body { width: 800px; height: 1200px; overflow: hidden; background: var(--backdrop); }
  .canvas { position: relative; width: 800px; height: 1200px; background: var(--backdrop); }
  .botanical-backdrop {
    position: absolute; inset: 0;
    background: radial-gradient(ellipse at 30% 30%, var(--backdrop-art), var(--backdrop) 60%),
                radial-gradient(ellipse at 75% 60%, var(--backdrop-art), transparent 55%);
  }
  .label { position: absolute; left: 170px; width: 460px; height: 333px; }
  .label--amber { top: 50px; --accent: var(--lavender); --art: var(--art-lavender); }
  .label--copper { top: 434px; --accent: var(--sage); --art: var(--art-sage); }
  .label--velvet { top: 817px; --accent: var(--olive); --art: var(--art-olive); }
  .label svg { display: block; }
  .accent-fill { fill: var(--accent); }
  .paper-fill { fill: var(--paper); }
  .art-fill { fill: var(--art); }
  .product-name { font-family: "Saira Condensed", sans-serif; font-weight: 400; fill: var(--paper); }
  .range-name { font-family: "Jost", sans-serif; font-style: italic; font-size: 13px; letter-spacing: 1px; fill: var(--paper); }
  .product-type { font-family: "Jost", sans-serif; font-weight: 500; font-size: 24px; letter-spacing: 6px; fill: var(--accent); }
  .scent { font-family: "Saira Condensed", sans-serif; font-size: 18px; letter-spacing: 0.5px; fill: var(--accent); }
  .pill-text { font-family: "Jost", sans-serif; font-weight: 500; font-size: 7.5px; fill: var(--paper); }
  .claims { font-family: "Jost", sans-serif; font-style: italic; font-size: 13px; fill: var(--paper); }
  .ingredients { font-family: "Jost", sans-serif; font-size: 6.4px; letter-spacing: 0.5px; fill: var(--accent); }
</style>
</head>
<body>
<div class="canvas">
  <div class="botanical-backdrop" role="img" aria-label="Faint engraved botanical backdrop of orchid, mint leaves and citrus slices"></div>

  <!-- label template repeated per scent -->
  <div class="label label--amber">
    <svg width="460" height="333" viewBox="0 0 460 333">
      <rect class="paper-fill" width="460" height="333"/>
      <rect class="accent-fill" width="111" height="333"/>
      <rect class="paper-fill" x="105" y="142" width="2" height="191"/>
      <text class="product-name" font-size="48" textLength="300" lengthAdjust="spacing" transform="translate(70,316) rotate(-90)">AMBER TIDE</text>
      <text class="range-name" transform="translate(102,140) rotate(-90)">Aromatherapy</text>
      <text class="product-type" x="232" y="38" text-anchor="middle">BODY BALM</text>
      <path class="accent-fill" d="M187 270 V99 A43.5 43.5 0 0 1 274 99 V270 Z"/>
      <rect class="art-fill" x="138" y="78" width="184" height="172" rx="20" opacity="0.85" role="img" aria-label="Engraved illustration of vanilla flower and lavender sprigs"/>
      <text class="scent" x="232" y="296" text-anchor="middle">Lavender + Vanilla</text>
      <path class="accent-fill" d="M187 333 V317 A6 6 0 0 1 193 311 H268 A6 6 0 0 1 274 317 V333 Z"/>
      <text class="pill-text" x="230.5" y="325" text-anchor="middle">100% NATURAL</text>
      <rect class="accent-fill" x="350" width="18" height="333"/>
      <text class="claims" text-anchor="middle" transform="translate(364,166) rotate(-90)">plant based  •  vegan  •  cruelty free</text>
      <g class="ingredients" text-anchor="middle">
        <text transform="translate(386,166) rotate(-90)">INGREDIENTS:</text>
        <text transform="translate(396,166) rotate(-90)">Organic Olive Fruit Oil (olea Europea), organic Coconut Oil</text>
        <text transform="translate(405,166) rotate(-90)">(Cocos Nucifera), Organic Shea Butter (Butyrospermum Parkii),</text>
        <text transform="translate(414,166) rotate(-90)">Organic Jojoba Seed Oil (Simmondsia Chinensis), Rosehip Seed Oil</text>
        <text transform="translate(423,166) rotate(-90)">(Rosa Canina), Vitamin E (Tocopherol), Sunflower Seed Oil</text>
        <text transform="translate(432,166) rotate(-90)">(Helianthus Annuus), Vanilla Aroma, Mentha Piperita (Peppermint)</text>
        <text transform="translate(441,166) rotate(-90)">Leaf Oil, Dipteryx Odorata (Tonka Bean) Oil</text>
      </g>
    </svg>
  </div>

  <div class="label label--copper">
    <svg width="460" height="333" viewBox="0 0 460 333">
      <rect class="paper-fill" width="460" height="333"/>
      <rect class="accent-fill" width="111" height="333"/>
      <rect class="paper-fill" x="105" y="142" width="2" height="191"/>
      <text class="product-name" font-size="44" textLength="304" lengthAdjust="spacingAndGlyphs" transform="translate(70,318) rotate(-90)">COPPER HARBOR</text>
      <text class="range-name" transform="translate(102,140) rotate(-90)">Aromatherapy</text>
      <text class="product-type" x="232" y="38" text-anchor="middle">BODY BALM</text>
      <path class="accent-fill" d="M187 270 V99 A43.5 43.5 0 0 1 274 99 V270 Z"/>
      <rect class="art-fill" x="138" y="78" width="184" height="172" rx="20" opacity="0.85" role="img" aria-label="Engraved illustration of eucalyptus branch and mint leaves"/>
      <text class="scent" x="232" y="296" text-anchor="middle">Eucalyptus + Mint</text>
      <path class="accent-fill" d="M187 333 V317 A6 6 0 0 1 193 311 H268 A6 6 0 0 1 274 317 V333 Z"/>
      <text class="pill-text" x="230.5" y="325" text-anchor="middle">100% NATURAL</text>
      <rect class="accent-fill" x="350" width="18" height="333"/>
      <text class="claims" text-anchor="middle" transform="translate(364,166) rotate(-90)">plant based  •  vegan  •  cruelty free</text>
      <g class="ingredients" text-anchor="middle">
        <text transform="translate(386,166) rotate(-90)">INGREDIENTS:</text>
        <text transform="translate(396,166) rotate(-90)">Organic Olive Fruit Oil (olea Europea), organic Coconut Oil</text>
        <text transform="translate(405,166) rotate(-90)">(Cocos Nucifera), Organic Shea Butter (Butyrospermum Parkii),</text>
        <text transform="translate(414,166) rotate(-90)">Organic Jojoba Seed Oil (Simmondsia Chinensis), Rosehip Seed Oil</text>
        <text transform="translate(423,166) rotate(-90)">(Rosa Canina), Vitamin E (Tocopherol), Sunflower Seed Oil</text>
        <text transform="translate(432,166) rotate(-90)">(Helianthus Annuus), Vanilla Aroma, Mentha Piperita (Peppermint)</text>
        <text transform="translate(441,166) rotate(-90)">Leaf Oil, Dipteryx Odorata (Tonka Bean) Oil</text>
      </g>
    </svg>
  </div>

  <div class="label label--velvet">
    <svg width="460" height="333" viewBox="0 0 460 333">
      <rect class="paper-fill" width="460" height="333"/>
      <rect class="accent-fill" width="111" height="333"/>
      <rect class="paper-fill" x="105" y="142" width="2" height="191"/>
      <text class="product-name" font-size="48" textLength="300" lengthAdjust="spacing" transform="translate(70,316) rotate(-90)">VELVET ARC</text>
      <text class="range-name" transform="translate(102,140) rotate(-90)">Aromatherapy</text>
      <text class="product-type" x="232" y="38" text-anchor="middle">BODY BALM</text>
      <path class="accent-fill" d="M187 270 V99 A43.5 43.5 0 0 1 274 99 V270 Z"/>
      <rect class="art-fill" x="138" y="78" width="184" height="172" rx="20" opacity="0.85" role="img" aria-label="Engraved illustration of bergamot fruit, citrus slice, leaves and cedar log"/>
      <text class="scent" x="232" y="296" text-anchor="middle">Bergamot + Cedarwood</text>
      <path class="accent-fill" d="M187 333 V317 A6 6 0 0 1 193 311 H268 A6 6 0 0 1 274 317 V333 Z"/>
      <text class="pill-text" x="230.5" y="325" text-anchor="middle">100% NATURAL</text>
      <rect class="accent-fill" x="350" width="18" height="333"/>
      <text class="claims" text-anchor="middle" transform="translate(364,166) rotate(-90)">plant based  •  vegan  •  cruelty free</text>
      <g class="ingredients" text-anchor="middle">
        <text transform="translate(386,166) rotate(-90)">INGREDIENTS:</text>
        <text transform="translate(396,166) rotate(-90)">Organic Olive Fruit Oil (olea Europea), organic Coconut Oil</text>
        <text transform="translate(405,166) rotate(-90)">(Cocos Nucifera), Organic Shea Butter (Butyrospermum Parkii),</text>
        <text transform="translate(414,166) rotate(-90)">Organic Jojoba Seed Oil (Simmondsia Chinensis), Rosehip Seed Oil</text>
        <text transform="translate(423,166) rotate(-90)">(Rosa Canina), Vitamin E (Tocopherol), Sunflower Seed Oil</text>
        <text transform="translate(432,166) rotate(-90)">(Helianthus Annuus), Vanilla Aroma, Mentha Piperita (Peppermint)</text>
        <text transform="translate(441,166) rotate(-90)">Leaf Oil, Dipteryx Odorata (Tonka Bean) Oil</text>
      </g>
    </svg>
  </div>
</div>
</body>
</html>
```